Australian Meat, Seafood and Fresh Produce Website

Our organization is looking to design a simple, but eye catching website to show our services.
Our company exports West Australian FRESH fruit and vegetables, seafood and meat.
The website we are looking for would consist of:
- Landing Page
- Company info
- Directors bio
- Page that highlights our products
- Contact us page
We would like it to have a Chinese translated version as well.
Tobin
Target Market(s)
Chinese Market
Industry/Entity Type
It Company
Number of Pages Required
1 page
Look and feel
Each slider illustrates characteristics of the customer's brand and the style your logo design should communicate.

```html
<!DOCTYPE html>
<html lang="en">
<head>
<meta charset="utf-8">
<title>Swan Coast Provisions</title>
<link rel="stylesheet" href="https://fonts.googleapis.com/css2?family=Mulish:wght@400;600;700;800&display=swap">
<style>
:root{
  --orange:#f07e0d;
  --teal:#36ab93;
  --teal-light:#4fbba4;
  --ink:#333333;
  --muted:#555555;
  --grey-band:#eeeeee;
  --white:#ffffff;
  --line:#d6d6d6;
}
*{box-sizing:border-box;margin:0;padding:0}
html,body{width:1200px;height:2169px;overflow:hidden;background:var(--white)}
body{position:relative;font-family:"Mulish",sans-serif;color:var(--ink)}
.abs{position:absolute}
.top-rule{left:0;top:0;width:1200px;height:3px;background:var(--orange)}
.brand{left:137px;top:20px;display:flex;align-items:center;gap:14px}
.brand-dot{width:54px;height:54px;border-radius:50%;background:var(--orange)}
.brand-text{font-weight:800;font-size:38px;color:var(--orange);letter-spacing:1px}
.nav{left:460px;top:0;display:flex;height:87px;align-items:stretch}
.nav a{color:var(--ink);text-decoration:none;font-weight:700;font-size:13px;display:flex;align-items:center;padding:0 17px;margin-top:0}
.nav a.active{background:var(--orange);color:var(--white);width:72px;justify-content:center;flex-direction:column;gap:6px;padding:0;border-radius:0 0 4px 4px}
.hero{left:0;top:107px;width:1200px;height:431px;background:var(--grey-band)}
.hero-visual{left:518px;top:107px;width:682px;height:431px;background:radial-gradient(ellipse at 50% 50%,#b9b7b2 0%,#d9cfc4 45%,var(--grey-band) 78%)}
.kicker{left:137px;top:226px;font-size:23px;font-weight:700;color:var(--teal)}
.hero-title{left:137px;top:254px;font-size:39px;font-weight:800;color:var(--orange)}
.hero-copy{left:137px;top:307px;width:365px;font-size:15px;line-height:17.5px;color:var(--ink)}
.btn{display:inline-flex;align-items:center;justify-content:center;background:var(--orange);color:var(--white);font-weight:800;font-size:12px;border-radius:4px;text-decoration:none}
.hero-btn{left:137px;top:403px;width:152px;height:37px;font-size:13px}
.section-title{left:0;width:1200px;text-align:center;font-size:34px;font-weight:700}
.t-teal{color:var(--teal)}
.t-orange{color:var(--orange)}
.centre-copy{left:137px;width:926px;text-align:center;font-size:15px;line-height:17.5px;color:var(--ink)}
.mgmt-band{left:0;top:957px;width:1200px;height:547px;background:var(--grey-band)}
.produce{left:166px;top:795px;width:875px;height:177px;border-radius:90px 90px 40px 40px;background:linear-gradient(90deg,#b23b2a,#e7b52a 30%,#f1a227 50%,#7fb83a 65%,#e4c21c 80%,#d9553c)}
.card{top:1106px;width:221px;height:328px;background:var(--white);border-radius:4px;overflow:hidden;text-align:center}
.card-photo{height:155px;background:linear-gradient(160deg,#4a2d1c,#a0683e 55%,#2d1a10)}
.card-name{margin-top:15px;font-size:16px;font-weight:800;color:var(--teal)}
.card-bio{margin:5px 14px 0;font-size:13px;line-height:15px;color:var(--ink);height:60px;overflow:hidden}
.card .btn{width:97px;height:31px;margin-top:14px}
.tabs{left:137px;top:1567px;width:926px;height:48px;border-bottom:1px solid var(--line);display:flex;justify-content:center}
.tab{width:170px;display:flex;align-items:center;justify-content:center;font-size:18px;font-weight:700;color:var(--ink)}
.tab.active{color:var(--teal);border:1px solid var(--line);border-bottom:1px solid var(--white);margin-bottom:-1px;background:var(--white)}
.suppliers{left:0;top:1885px;width:1200px;height:105px;background:var(--teal)}
.sup-title{left:137px;top:1908px;color:var(--white);font-size:26px;font-weight:700}
.sup-sub{left:137px;top:1943px;color:var(--white);font-size:14px}
.sup-cells{left:406px;top:1885px;width:657px;height:105px;display:flex}
.sup-cell{flex:1;background:var(--teal-light);border-left:1px solid var(--teal);display:flex;flex-direction:column;align-items:center;justify-content:center;color:var(--white)}
.sup-cell a{color:var(--white);font-size:14px}
.sup-cell span{font-size:11px;margin-top:6px}
.footer{left:0;top:1990px;width:1200px;height:138px;background:var(--grey-band)}
.foot-head{top:2035px;font-size:14px;font-weight:800;color:var(--orange)}
.foot-rule{top:2071px;height:1px;background:var(--line)}
.foot-links{left:137px;top:2088px;display:flex;gap:34px;font-size:12px;color:var(--ink)}
.social{left:928px;top:2085px;display:flex;gap:6px}
.social span{width:21px;height:21px;border-radius:50%;background:#2e2e2e}
.legal{top:2141px;font-size:11px;color:var(--ink)}
</style>
</head>
<body>
<div class="abs top-rule"></div>

<header>
  <div class="abs brand"><span class="brand-dot"></span><span class="brand-text">SCP</span></div>
  <nav class="abs nav">
    <a class="active" href="#">
      <svg width="18" height="16" viewBox="0 0 18 16" aria-hidden="true"><path d="M9 1 1 8h2.5v7h4v-5h3v5h4V8H17z" fill="#fff"/></svg>
      HOME</a>
    <a href="#">ABOUT SCP</a>
    <a href="#">THE MANAGEMENT TEAM</a>
    <a href="#">SUPPLIERS</a>
    <a href="#">CONTACT US</a>
  </nav>
</header>

<section>
  <div class="abs hero"></div>
  <div class="abs hero-visual" role="img" aria-label="Photograph of fresh whole fish, prawns, shellfish and octopus"></div>
  <div class="abs kicker">WELCOME TO</div>
  <h1 class="abs hero-title">SWAN COAST PROVISIONS</h1>
  <p class="abs hero-copy">Swan Coast Provisions (SCP) aims to supply high quality West Australian produce to the rest of the World. Western Australia is known for its high quality farming practices and environment,</p>
  <a class="abs btn hero-btn" href="#">READ MORE</a>
</section>

<section>
  <h2 class="abs section-title t-teal" style="top:592px">ABOUT SCP</h2>
  <p class="abs centre-copy" style="top:648px">Swan Coast Provisions (SCP) aims to supply high quality West Australian produce to the rest of the World. Western Australia is known for its high quality farming practices and environment, which produces meat, seafood, fruit and vegetable of a caliber that is respected globally.<br>With a management team and first class suppliers allows our organization to provide quality ingredients, straight from farm or ocean to purchaser, in a timely manner to the highest quality.<br>This document aims to outline both our management team and their back grounds, as well as the suppliers who will initially be supply our global customers.</p>
</section>

<div class="abs mgmt-band"></div>
<div class="abs produce" role="img" aria-label="Photograph of an assortment of fresh fruit and vegetables"></div>

<section>
  <h2 class="abs section-title t-orange" style="top:1032px">THE MANAGEMENT TEAM</h2>
  <article class="abs card" style="left:137px">
    <div class="card-photo" role="img" aria-label="Portrait photograph of Jared Tobin"></div>
    <h3 class="card-name">JARED TOBIN</h3>
    <p class="card-bio">Jared brings with him decades of experience in hospitality management, specializing in remote service and major city</p>
    <a class="btn" href="#">READ MORE</a>
  </article>
  <article class="abs card" style="left:372px">
    <div class="card-photo" role="img" aria-label="Portrait photograph of Marcus Hale"></div>
    <h3 class="card-name">MARCUS HALE</h3>
    <p class="card-bio">Marcus has been in the Sales, Retail &amp; Procurement since 1972, after leaving Senior High School started Sales in the Tobacco</p>
    <a class="btn" href="#">READ MORE</a>
  </article>
  <article class="abs card" style="left:607px">
    <div class="card-photo" role="img" aria-label="Portrait photograph of Owen Pritchard"></div>
    <h3 class="card-name">OWEN PRITCHARD</h3>
    <p class="card-bio">Senior Executive with entrepreneurial experience in company building mainly in the transport and logistics field.</p>
    <a class="btn" href="#">READ MORE</a>
  </article>
  <article class="abs card" style="left:842px">
    <div class="card-photo" role="img" aria-label="Portrait photograph of Dr Meiling Zhou"></div>
    <h3 class="card-name">DR MEILING ZHOU</h3>
    <p class="card-bio">Well respected senior professional in the health and business community of Shunde Peoples Republic of China.</p>
    <a class="btn" href="#">READ MORE</a>
  </article>
</section>

<section>
  <div class="abs tabs">
    <div class="tab">Vision and Mission</div>
    <div class="tab active">SCP History</div>
    <div class="tab">SCP Worldwide</div>
  </div>
  <h2 class="abs section-title t-orange" style="top:1655px">SCP History</h2>
  <p class="abs centre-copy" style="top:1728px">Swan Coast Provisions (SCP) aims to supply high quality West Australian produce to the rest of the World. Western Australia is known for its high quality farming practices and environment, which produces meat, seafood, fruit and vegetable of a caliber that is respected globally.<br>With a management team and first class suppliers allows our organization to provide quality ingredients, straight from farm or ocean to purchaser, in a timely manner to the highest quality.<br>This document aims to outline both our management team and their back grounds, as well as the suppliers who will initially be supply our global customers.</p>
</section>

<section>
  <div class="abs suppliers"></div>
  <h2 class="abs sup-title">Suppliers</h2>
  <p class="abs sup-sub">The suppliers SCP will be using are:</p>
  <div class="abs sup-cells">
    <div class="sup-cell"><a href="#">Harbour Line Distributors</a><span>High quality beef, lamb and pork</span></div>
    <div class="sup-cell"><a href="#">www.greenrowfarms.com.au</a><span>Fresh Fruit and Vegetables</span></div>
    <div class="sup-cell"><a href="#">www.bluereefcatch.com.au</a><span>Fresh Seafood</span></div>
  </div>
</section>

<footer>
  <div class="abs footer"></div>
  <div class="abs foot-head" style="left:137px">QUICK LINKS</div>
  <div class="abs foot-rule" style="left:137px;width:524px"></div>
  <div class="abs foot-links"><span>HOME</span><span>ABOUT SCP</span><span>THE MANAGEMENT TEAM</span><span>SUPPLIERS</span><span>CONTACT US</span></div>
  <div class="abs foot-head" style="left:928px">FOLLOW US</div>
  <div class="abs foot-rule" style="left:928px;width:135px"></div>
  <div class="abs social"><span></span><span></span><span></span><span></span><span></span></div>
  <div class="abs legal" style="left:137px">Copyright © 2015 - All rights reserved</div>
  <div class="abs legal" style="left:862px">Terms and Conditions &nbsp;&nbsp;|&nbsp;&nbsp; Privacy policy</div>
</footer>
</body>
</html>
```